Cover for "ROOTED! The skill and rhythm of guiding teams through calm and delight"

My first book for a global audience of modern performance leaders needs its cover!
I am an international executive coach and I've developed a new approach to replace classic Performance Management with a natural, sustainable approach fit for human beings :) My first book is about this approach and serves two purposes: helping leaders and sparking their curiosity to learn more, and positioning myself as a thought leader in the field.
The book is built on personal experience; it is both professional and personal ("From me to You"), and I'd like to position it beyond classic categorisation.
Its cover should communicate humanness, naturalness, ease and joy, within an unmistakably business-y context. I would like to see designs that use the color yellow (but not sure it communicates the right things).
Updates

Target Market(s)

Leaders who aspire to have a positive impact and deliver results in a meaningful way

Industry/Entity Type

Consulting & Executive Coaching - Trusted Advisor

Font styles to use
Other font styles liked:
• Helvetica Neue

Colors
0094D4
00A9DD
6FCCEA
C7EBF8
E9F6FB
FFC000
F8CF3A
FAE287
FDF2CF
FEFAEE
EE7325
F08F49
F5BC92
FAE3D3
FDF4ED

Requirements
Must have
• A both-and feeling to it (see description), e.g., masculine AND feminine, business AND humanness. Power with, not power over...
Should not have
• Too much "bling" - no classic status symbol business success language

```html
<!DOCTYPE html>
<html lang="en">
<head>
<meta charset="utf-8">
<title>ROOTED! — Book Cover</title>
<link rel="stylesheet" href="https://fonts.googleapis.com/css2?family=Alfa+Slab+One&family=Montserrat:ital,wght@1,700&family=Jost:wght@400&display=swap">
<style>
  :root {
    --page-bg: #ffffff;
    --orange-deep: #ee7325;
    --yellow-core: #ffc000;
    --yellow-soft: #f8cf3a;
    --ink-light: #ffffff;
    --photo-dark: #2b2523;
    --photo-warm: #a8744f;
  }
  html, body {
    margin: 0;
    padding: 0;
    width: 1200px;
    height: 432px;
    overflow: hidden;
    background: var(--page-bg);
  }
  .stage {
    width: 1200px;
    height: 432px;
    display: flex;
    align-items: center;
    justify-content: center;
  }
  .book-cover {
    width: 267px;
    height: 400px;
    display: block;
    box-shadow: 0 2px 8px rgba(0,0,0,0.12);
  }
  .title { font-family: "Alfa Slab One", "Roboto Slab", serif; }
  .subtitle { font-family: "Montserrat", "Helvetica Neue", sans-serif; font-style: italic; font-weight: 700; }
  .author { font-family: "Jost", "Helvetica Neue", sans-serif; font-weight: 400; letter-spacing: 2px; }
</style>
</head>
<body>
<main class="stage">
  <svg class="book-cover" viewBox="0 0 581 870" xmlns="http://www.w3.org/2000/svg" aria-label="Book cover: ROOTED! The skill and rhythm of guiding teams through calm and delight">
    <defs>
      <radialGradient id="cover-glow" cx="50%" cy="52%" r="70%">
        <stop offset="0%" stop-color="var(--yellow-core)"/>
        <stop offset="45%" stop-color="var(--yellow-soft)" stop-opacity="0.9"/>
        <stop offset="100%" stop-color="var(--orange-deep)"/>
      </radialGradient>
      <radialGradient id="photo-tones" cx="50%" cy="55%" r="60%">
        <stop offset="0%" stop-color="var(--photo-warm)"/>
        <stop offset="100%" stop-color="var(--photo-dark)"/>
      </radialGradient>
      <linearGradient id="photo-fade" x1="0" y1="0" x2="0" y2="1">
        <stop offset="0%" stop-color="#fff" stop-opacity="0"/>
        <stop offset="18%" stop-color="#fff" stop-opacity="1"/>
        <stop offset="82%" stop-color="#fff" stop-opacity="1"/>
        <stop offset="100%" stop-color="#fff" stop-opacity="0"/>
      </linearGradient>
      <mask id="photo-mask">
        <rect x="0" y="405" width="581" height="330" fill="url(#photo-fade)"/>
      </mask>
    </defs>

    <rect class="cover-background" width="581" height="870" fill="url(#cover-glow)"/>

    <g class="title-echoes" fill="var(--ink-light)">
      <text class="title" x="290" y="318" text-anchor="middle" font-size="128" textLength="520" lengthAdjust="spacingAndGlyphs" opacity="0.38">ROOTED!</text>
      <text class="title" x="290" y="428" text-anchor="middle" font-size="128" textLength="520" lengthAdjust="spacingAndGlyphs" opacity="0.3">ROOTED!</text>
      <text class="title" x="290" y="538" text-anchor="middle" font-size="128" textLength="520" lengthAdjust="spacingAndGlyphs" opacity="0.22">ROOTED!</text>
      <text class="title" x="290" y="648" text-anchor="middle" font-size="128" textLength="520" lengthAdjust="spacingAndGlyphs" opacity="0.16">ROOTED!</text>
      <text class="title" x="290" y="745" text-anchor="middle" font-size="128" textLength="520" lengthAdjust="spacingAndGlyphs" opacity="0.1">ROOTED!</text>
    </g>

    <rect class="handshake-photo" role="img" aria-label="Photo of two business people in dark suits shaking hands across the cover"
          x="0" y="405" width="581" height="330" fill="url(#photo-tones)" mask="url(#photo-mask)" opacity="0.92"/>

    <text class="title" x="290" y="205" text-anchor="middle" font-size="128" textLength="520" lengthAdjust="spacingAndGlyphs" fill="var(--ink-light)">ROOTED!</text>

    <g class="subtitle" fill="var(--ink-light)" font-size="22" text-anchor="middle">
      <text x="290" y="760" textLength="520" lengthAdjust="spacingAndGlyphs">THE SKILL AND RHYTHM OF GUIDING TEAMS</text>
      <text x="290" y="784">THROUGH CALM AND DELIGHT</text>
    </g>

    <text class="author" x="296" y="853" text-anchor="middle" font-size="33" fill="var(--ink-light)">AUTHOR NAME</text>
  </svg>
</main>
</body>
</html>
```